THE POINT AT MAPLE SWALE HUDSON RIVER WATERFRONT LAND

crisp clear business cards on wood stock or thick paper with large font with a river otter logo, PERSONAL INFO ON ONE SIDE, PROJECT INFO ON THE OTHER SIDE
Updates

I don’t have a logo. Just thought that a photo of a river otter would look appealing.

Target Market(s)

Buyers and realtors

Industry/Entity Type

Real Estate Development

Contact Information for Business Card

MARTIN OSGOOD
518-730-4862 (Call or Text)
STONE HAVEN LLC PRINCIPAL

MOSHAVENRD@TARNMAIL.COM

Font styles to use
Sans Serif

Colors
fbfdfe
0792cd
00a990
fbed22
ec1f27

Requirements
Must have
• LARGE FONT, ROUNDED EDGES,
Nice to have
• ON THE BACK SIDE :
• THE POINT AT MAPLE SWALE
• HUDSON RIVER WATERFRONT LAND
• 2 TO 67 ACRES---READY TO BUILD
• PRICED TO SELL!

```html
<!DOCTYPE html>
<html lang="en">
<head>
<meta charset="utf-8">
<title>Stone Haven LLC – Business Cards</title>
<link rel="stylesheet" href="https://fonts.googleapis.com/css2?family=Roboto:wght@400;500;700&display=swap">
<style>
  :root {
    --backdrop: #595b5d;
    --paper: #fbfdfe;
    --teal: #00a990;
    --blue: #0792cd;
    --ink: #2b2b2b;
    --rule: #8a8a8a;
  }
  * { margin: 0; padding: 0; box-sizing: border-box; }
  html, body {
    width: 1200px;
    height: 802px;
    overflow: hidden;
    background: var(--backdrop);
    font-family: "Roboto", Arial, sans-serif;
  }
  .card-set {
    position: relative;
    width: 1200px;
    height: 802px;
  }
  .card {
    position: absolute;
    top: 274px;
    width: 442px;
    height: 265px;
    box-shadow: 2px 3px 6px rgba(0, 0, 0, 0.45);
    overflow: hidden;
  }
  /* Personal side */
  .card--personal {
    left: 136px;
    background: var(--teal);
    color: var(--paper);
    text-align: right;
    padding-right: 30px;
  }
  .holder-name {
    position: absolute;
    right: 30px;
    top: 47px;
    font-size: 19.5px;
    font-weight: 500;
    letter-spacing: 0.2px;
  }
  .holder-title {
    position: absolute;
    right: 30px;
    top: 70px;
    font-size: 12.5px;
    font-weight: 400;
  }
  .contact-phone {
    position: absolute;
    right: 30px;
    top: 106px;
    font-size: 13.5px;
    font-weight: 400;
  }
  .contact-phone strong {
    font-size: 15.5px;
    font-weight: 700;
  }
  .contact-email {
    position: absolute;
    right: 30px;
    top: 129px;
    font-size: 12.5px;
    font-weight: 400;
  }
  .contact-email strong { font-weight: 500; }
  /* Project side */
  .card--project {
    left: 624px;
    background: var(--paper);
    color: var(--ink);
    text-align: center;
  }
  .brand-dot {
    position: absolute;
    left: 191px;
    top: 52px;
    width: 60px;
    height: 60px;
    border-radius: 50%;
    background: var(--blue);
  }
  .brand-name {
    position: absolute;
    left: 0;
    right: 0;
    top: 134px;
    font-size: 34px;
    font-weight: 700;
    color: var(--teal);
    letter-spacing: -0.5px;
  }
  .brand-rule {
    position: absolute;
    left: 66px;
    width: 311px;
    top: 183px;
    height: 1px;
    background: var(--rule);
  }
  .project-lines {
    position: absolute;
    left: 0;
    right: 0;
    top: 192px;
    list-style: none;
    font-size: 12.5px;
    line-height: 17.5px;
  }
</style>
</head>
<body>
<main class="card-set">
  <section class="card card--personal" aria-label="Personal side">
    <h1 class="holder-name">MARTIN OSGOOD</h1>
    <p class="holder-title">PRINCIPAL</p>
    <p class="contact-phone"><strong>Call or Text</strong> : 518-730-4862</p>
    <p class="contact-email"><strong>E:</strong> MOSHAVENRD@TARNMAIL.COM</p>
  </section>

  <section class="card card--project" aria-label="Project side">
    <span class="brand-dot" aria-hidden="true"></span>
    <h2 class="brand-name">STONE HAVEN LLC</h2>
    <div class="brand-rule"></div>
    <ul class="project-lines">
      <li>THE POINT AT MAPLE SWALE</li>
      <li>HUDSON RIVER WATERFRONT LAND</li>
      <li>2 TO 67 ACRES---READY TO BUILD | PRICED TO SELL!</li>
    </ul>
  </section>
</main>
</body>
</html>
```